Business Card cabinets and cabinets components making company.

the card should be formal and interesting at the same time. The main colors will be black and white.

Font styles to use
Sans Serif

Colors

Designer to choose only greyscale colors for use in the design.

Requirements
Must have
• At least must have the followings:
office phone
cell phone
address
position
name
email
web

```html
<!DOCTYPE html>
<html lang="en">
<head>
<meta charset="utf-8">
<title>Joinwell Business Card</title>
<link rel="stylesheet" href="https://fonts.googleapis.com/css2?family=Nunito+Sans:wght@300;400;700&display=swap">
<style>
  :root {
    --page: #e9e8e6;
    --ink-dark: #3b3b3d;
    --card-light: #f2f2f4;
    --band: #e3e3e5;
    --band-edge: #cfcfd2;
    --text-dark: #3b3b3d;
    --text-light: #ffffff;
    --shadow: rgba(0, 0, 0, 0.18);
  }
  * { box-sizing: border-box; margin: 0; padding: 0; }
  html, body {
    width: 1131px;
    height: 1200px;
    overflow: hidden;
    background: var(--page);
    font-family: "Nunito Sans", Arial, sans-serif;
  }
  .canvas { position: relative; width: 1131px; height: 1200px; }
  .card {
    position: absolute;
    left: 216px;
    width: 778px;
    height: 444px;
    border-radius: 26px;
    overflow: hidden;
    box-shadow: 0 14px 26px var(--shadow);
  }
  .card--front { top: 57px; background: var(--card-light); }
  .card--back { top: 602px; background: var(--ink-dark); }
  .card__shapes { position: absolute; inset: 0; }
  .holder { position: absolute; left: 47px; color: var(--text-dark); }
  .holder__name { top: 84px; font-size: 24px; font-weight: 400; }
  .holder__role { top: 117px; font-size: 15px; font-weight: 400; }
  .address {
    position: absolute; left: 47px; top: 202px;
    color: var(--text-light); font-size: 16px; line-height: 22px;
    font-weight: 400; font-style: normal;
  }
  .contacts {
    position: absolute; left: 47px; top: 283px;
    list-style: none; color: var(--text-light);
    font-size: 18px; font-weight: 400;
  }
  .contacts li { display: flex; align-items: center; height: 25.5px; }
  .contacts svg { width: 14px; height: 14px; margin-right: 15px; fill: var(--text-light); flex: none; }
  .brand {
    position: absolute; display: flex; align-items: center;
    font-weight: 700; line-height: 1;
  }
  .brand__mark { display: block; background: currentColor; }
  .brand--small { left: 486px; top: 110px; font-size: 50px; color: var(--text-dark); }
  .brand--small .brand__mark { width: 26px; height: 26px; margin-right: 14px; }
  .brand--large {
    left: 0; right: 0; top: 150px; justify-content: center;
    font-size: 92px; color: var(--text-light);
  }
  .brand--large .brand__mark { width: 48px; height: 48px; margin-right: 22px; }
  .web {
    position: absolute; left: 0; right: 0; top: 392px;
    text-align: center; color: var(--text-light); font-size: 17px; font-weight: 400;
  }
</style>
</head>
<body>
<main class="canvas">

  <section class="card card--front">
    <svg class="card__shapes" width="778" height="444" viewBox="0 0 778 444">
      <polygon points="0,0 347,0 495,444 0,444" fill="var(--ink-dark)"/>
      <polygon points="0,70 386,70 412,149 0,149" fill="var(--band)"/>
      <polygon points="386,70 412,149 400,149 376,70" fill="var(--band-edge)"/>
    </svg>
    <p class="holder holder__name">Daniel Hart</p>
    <p class="holder holder__role">CEO/founder</p>
    <address class="address">48 Harlow Avenue,<br>3rd FL Brookdale,<br>NY 10452</address>
    <ul class="contacts">
      <li><svg viewBox="0 0 24 24"><path d="M6.6 10.8a15.1 15.1 0 0 0 6.6 6.6l2.2-2.2c.3-.3.7-.4 1-.2 1.1.4 2.3.6 3.6.6.6 0 1 .4 1 1V20c0 .6-.4 1-1 1C10.6 21 3 13.4 3 4c0-.6.4-1 1-1h3.5c.6 0 1 .4 1 1 0 1.3.2 2.5.6 3.6.1.3 0 .7-.2 1z"/></svg>+1 555 014 2318</li>
      <li><svg viewBox="0 0 24 24"><path d="M2 8c3-3 17-3 20 0l-1 3-4-1V8c-3-1-7-1-10 0v2l-4 1z"/><path d="M6 12h12l2 8H4z"/><circle cx="12" cy="16" r="2" fill="var(--ink-dark)"/></svg>+1 555 019 8220-4</li>
      <li><svg viewBox="0 0 24 24"><path d="M2 5h20v14H2z"/><path d="M2 5l10 8 10-8" fill="none" stroke="var(--ink-dark)" stroke-width="2"/></svg>d.hart@joinwellstudio.com</li>
      <li><svg viewBox="0 0 24 24"><rect x="3" y="3" width="18" height="18" rx="4"/></svg>joinwellstudio</li>
      <li><svg viewBox="0 0 24 24"><circle cx="12" cy="12" r="8"/></svg>social.joinwell.com</li>
    </ul>
    <div class="brand brand--small"><span class="brand__mark"></span>Joinwell</div>
  </section>

  <section class="card card--back">
    <div class="brand brand--large"><span class="brand__mark"></span>Joinwell</div>
    <p class="web">www.joinwellstudio.com</p>
  </section>

</main>
</body>
</html>
```